Wed site for biomedical device startup

We need a generic website for a medical device startup. I will provide examples below of websites from other companies that can serve as models for what we are looking for. The startup is for a device that can non invasively measure blood flow in the brain using light. The application is to detect the type of stroke someone is having before they get to the hospital so treatment can be started right away. This saves patients upto hours of delayed treatment. Patients will be able to recover from stroke much better and faster as a result. I have attached an AI generated illustration of what the device will ultimately look like for reference.

https://www.872vantora.com
https://quilvesta.com

Target Market(s)

Biomedical, medical device, investors of biomedical device startups

Industry/Entity Type

Biomedical

Coding

Coded - Design and coding required

Number of Pages Required

4 page

Requirements
Must have
• same section and section headings as example websites listed above
Nice to have
• similar to example websites listed above. Prefer a darker website over a lighter one. Perhaps dark blues to go with logo colors. A moving background image element at top of landing page could be cool. Something indicative of heartbeat, or neurons, or blood flow.

```html
<!DOCTYPE html>
<html lang="en">
<head>
<meta charset="utf-8">
<title>Cerevia — Technology for premature infants</title>
<link href="https://fonts.googleapis.com/css2?family=Lexend:wght@300;400;500&family=DM+Sans:wght@400;500&display=swap" rel="stylesheet">
<style>
:root{
  --navy:#05052e;
  --indigo:#10109a;
  --blue:#1c1ce0;
  --magenta:#b52fd8;
  --pink:#e26ae8;
  --cyan:#12d6e6;
  --ink:#14142a;
  --muted:#6d6d7c;
  --line:#e4e6ee;
  --paper:#ffffff;
  --mist:#f2f7fc;
  --head:"Lexend",sans-serif;
  --body:"DM Sans",sans-serif;
}
*{margin:0;padding:0;box-sizing:border-box}
html,body{width:1200px;height:1200px;overflow:hidden;background:var(--paper)}
body{position:relative;font-family:var(--body);color:var(--ink)}
.abs{position:absolute}
.hero-bg{background:radial-gradient(ellipse at 75% 85%,var(--blue) 0%,var(--indigo) 40%,var(--navy) 85%)}
.brand{font-family:var(--head);font-weight:400;color:#fff;display:flex;align-items:center}
.brand i{display:inline-block;border-radius:50%;background:var(--magenta)}

/* ===== main hero ===== */
.hero{left:273px;top:4px;width:919px;height:594px;border-radius:8px;overflow:hidden}
.hero .brand{left:38px;top:30px;font-size:20px;gap:6px}
.hero .brand i{width:22px;height:22px}
.nav{left:291px;top:38px;display:flex;gap:20px;font-family:var(--head);font-size:8.6px;letter-spacing:.9px;color:#fff}
.nav .active{color:var(--pink)}
.btn-outline-light{left:769px;top:25px;width:120px;height:34px;border:1.5px solid #fff;border-radius:4px;color:#fff;font-family:var(--head);font-size:10px;display:flex;align-items:center;justify-content:center}
.eyebrow{left:84px;top:164px;color:#fff;font-family:var(--head);font-size:8.4px;letter-spacing:1px}
.headline{left:83px;top:186px;font-family:var(--head);font-weight:400;font-size:45px;line-height:47px;color:#fff}
.headline span{color:var(--pink)}
.btn-primary{left:84px;top:399px;width:114px;height:36px;border-radius:5px;background:var(--magenta);color:#fff;font-family:var(--head);font-size:10px;display:flex;align-items:center;justify-content:center}
.hero-visual{left:519px;top:123px;width:316px;height:354px;border-radius:6px;background:linear-gradient(160deg,rgba(18,214,230,.55) 0%,rgba(150,130,200,.5) 45%,rgba(181,47,216,.6) 100%)}
.stat-card{left:484px;top:288px;width:206px;height:159px;border-radius:6px;background:rgba(190,50,220,.82);color:#fff;padding:0 26px}
.stat-card .num{font-family:var(--head);font-size:40px;margin-top:32px;letter-spacing:2px}
.stat-card hr{border:0;border-top:1px solid rgba(255,255,255,.7);margin-top:14px}
.stat-card p{font-family:var(--head);font-size:11.5px;margin-top:14px}
.divider{left:33px;top:528px;width:853px;border-top:1px solid rgba(255,255,255,.15)}
.marquee{left:-4px;top:553px;white-space:nowrap;color:#fff;font-family:var(--head);font-size:12px;letter-spacing:1.3px;display:flex;align-items:center;gap:30px}
.marquee b{display:inline-block;width:8px;height:8px;border:2.5px solid #fff;border-radius:50%}

/* ===== how we help ===== */
.help-title{left:284px;top:660px;font-family:var(--head);font-weight:400;font-size:26px;letter-spacing:.5px}
.help-copy{left:284px;top:710px;width:332px;font-size:10.3px;line-height:17px;color:var(--muted)}
.help-copy p+p{margin-top:16px}
.btn-outline-dark{left:284px;top:1066px;width:109px;height:35px;border:1.5px solid var(--ink);border-radius:4px;font-family:var(--head);font-size:10.5px;display:flex;align-items:center;justify-content:center}
.vrule{top:662px;height:438px;border-left:1px solid var(--line)}
.card-photo{top:662px;width:232px;height:244px;border-radius:6px}
.card-title{top:924px;font-family:var(--head);font-size:14px;font-weight:400}
.card-body{top:950px;width:236px;font-size:10.3px;line-height:17px;color:var(--muted)}
.card-body p+p{margin-top:16px}
.bottom-band{left:258px;top:1166px;width:942px;height:34px;background:var(--mist)}

/* ===== overview column ===== */
.mini{font-size:3.4px;line-height:4.6px;color:var(--muted)}
.t-hero{left:4px;top:4px;width:233px;height:150px;overflow:hidden}
.t-hero .brand{left:9px;top:9px;font-size:5.5px;gap:2px}
.t-hero .brand i{width:5px;height:5px}
.t-nav{left:74px;top:11px;display:flex;gap:6px;font-size:2.4px;color:#fff;font-family:var(--head)}
.t-btn{left:195px;top:7px;width:31px;height:9px;border:.6px solid #fff;border-radius:2px;font-size:2.6px;color:#fff;display:flex;align-items:center;justify-content:center}
.t-head{left:21px;top:50px;font-family:var(--head);font-weight:400;font-size:11.5px;line-height:12px;color:#fff}
.t-head span{color:var(--pink)}
.t-welcome{left:21px;top:41px;font-size:2.4px;color:#fff}
.t-cta{left:21px;top:101px;width:29px;height:9px;background:var(--magenta);border-radius:2px;font-size:2.4px;color:#fff;display:flex;align-items:center;justify-content:center}
.t-visual{left:132px;top:31px;width:85px;height:92px;border-radius:2px;background:linear-gradient(160deg,rgba(18,214,230,.55),rgba(150,130,200,.5) 45%,rgba(181,47,216,.6))}
.t-card{left:123px;top:73px;width:54px;height:42px;background:rgba(190,50,220,.82);border-radius:2px;color:#fff;padding:6px 6px}
.t-card b{font-family:var(--head);font-weight:400;font-size:11px}
.t-card p{font-size:2.4px;margin-top:6px}
.t-marquee{left:8px;top:141px;white-space:nowrap;font-size:2.6px;color:#fff;letter-spacing:.3px;font-family:var(--head)}

.t-help-title{left:6px;top:171px;font-family:var(--head);font-weight:400;font-size:6.5px}
.t-help-copy{left:6px;top:183px;width:84px}
.t-help-btn{left:6px;top:273px;width:28px;height:9px;border:.6px solid var(--ink);border-radius:2px;font-size:2.6px;display:flex;align-items:center;justify-content:center}
.t-photo{top:171px;width:59px;height:62px}
.t-cap{top:237px;font-size:3.2px;color:var(--ink)}
.t-capbody{top:243px;width:60px}

.t-welcome-band{left:0;top:299px;width:240px;height:183px;background:var(--mist)}
.t-wphoto{left:26px;top:324px;width:92px;height:121px}
.t-wlabel{left:137px;top:324px;font-size:2.4px;color:var(--ink)}
.t-wtext{left:137px;top:330px;width:95px;font-family:var(--head);font-weight:400;font-size:8px;line-height:9px}
.t-select{left:137px;top:384px;width:89px;height:8px;border:.6px solid #c9cbd6;background:#fff;font-size:2.4px;padding:2px 3px;display:flex;justify-content:space-between}
.t-partners{left:16px;top:471px;display:flex;gap:9px;align-items:center}
.t-partners span{display:block;height:7px;border-radius:2px;background:#d9c7e3}

.t-care{left:9px;top:493px;width:222px;height:149px}
.t-care-h{left:15px;font-family:var(--head);font-weight:400;font-size:7.5px;color:#fff}
.t-care-list{left:15px;width:90px;color:#eee;font-size:2.4px;line-height:4.2px}

.t-arc{left:-78px;top:645px;width:152px;height:188px;border-radius:50%;background:#edf4fb}
.t-team{width:68px;height:68px}
.t-name{font-size:2.8px;color:var(--ink)}
.t-role{font-size:2.2px;color:#9a9aa8}

.t-contact{left:9px;top:859px;width:222px;height:137px}
.t-form{left:141px;top:872px;width:85px;height:111px;background:#fff;border-radius:3px;padding:7px 5px}
.t-form h4{font-family:var(--head);font-weight:400;font-size:4.6px;line-height:5.6px}
.t-field{height:9px;border-bottom:.6px solid #dfe1ea;font-size:2.2px;color:#aaa;padding-top:3px}
.t-send{height:8px;background:var(--magenta);border-radius:2px;color:#fff;font-size:2.4px;display:flex;align-items:center;justify-content:center;margin-top:5px}

.t-faq-orb{left:2px;top:1040px;width:92px;height:74px;border-radius:50%;background:radial-gradient(circle,#f3e9fa 0%,#eef4fb 60%,rgba(255,255,255,0) 72%)}
.t-faq-label{left:14px;top:1019px;font-size:2.2px}
.t-faq-title{left:14px;top:1024px;font-family:var(--head);font-weight:400;font-size:8px;line-height:9px}
.t-faq-copy{left:14px;top:1048px;width:92px}
.t-faq-list{left:123px;top:1024px;width:103px}
.t-faq-list div{font-size:2.8px;border-bottom:.6px solid var(--line);padding:4px 0;display:flex;justify-content:space-between}

.t-footer{left:4px;top:1117px;width:233px;height:83px;background:var(--navy);color:#fff}
.t-footer .brand{left:14px;top:21px;font-size:9px;gap:3px}
.t-footer .brand i{width:9px;height:9px}
.t-fcol{top:18px;font-size:2.6px;line-height:4.4px}
.t-fsoc{display:flex;gap:5px;margin-top:5px}
.t-fsoc i{width:4px;height:4px;border-radius:50%;background:#fff;display:block}
.t-fbase{left:10px;top:75px;width:215px;font-size:2.2px;display:flex;justify-content:space-between}
</style>
</head>
<body>

<!-- ===== Overview column ===== -->
<section class="abs t-hero hero-bg">
  <div class="abs brand"><i></i>Cerevia</div>
  <nav class="abs t-nav"><span style="color:var(--pink)">HOME</span><span>ABOUT</span><span>TECHNOLOGY</span><span>PUBLICATIONS</span><span>CONTACT</span></nav>
  <div class="abs t-btn">Get in Touch</div>
  <div class="abs t-welcome">WELCOME TO CEREVIA · STARTUP</div>
  <div class="abs t-visual" role="img" aria-label="Doctor greeting a young child in front of a colourful backdrop"></div>
  <h1 class="abs t-head">Improving the<br>future for the<br><span>smallest<br>patients</span></h1>
  <div class="abs t-cta">More Details</div>
  <div class="abs t-card"><b>20+</b><p>Years of experience</p></div>
  <div class="abs t-marquee">● TECHNOLOGY FOR PREMATURE INFANTS &nbsp; ● TECHNOLOGY FOR PREMATURE INFANTS &nbsp; ● TECHNOLOGY FOR PREMATURE INFANTS</div>
</section>

<section>
  <h2 class="abs t-help-title">HOW WE HELP</h2>
  <div class="abs t-help-copy mini">During the first days of life a significant risk of permanent injury exists from ventricular hemorrhage caused by rupture of immature blood vessels.<br><br>VELIX is a continuous intracranial blood flow sensor giving clinicians an early warning signal.</div>
  <div class="abs t-help-btn">Contact Us</div>
  <div class="abs" style="left:96px;top:171px;height:112px;border-left:.6px solid var(--line)"></div>
  <div class="abs t-photo" role="img" aria-label="Newborn on a blue blanket held by clinician hands" style="left:103px;background:linear-gradient(160deg,#d9b59a,#3d5f9c)"></div>
  <div class="abs t-photo" role="img" aria-label="Premature infant with feeding tube" style="left:175px;background:linear-gradient(160deg,#e0c5b0,#b06a55)"></div>
  <div class="abs t-cap" style="left:103px">What is it VELIX</div>
  <div class="abs t-capbody mini" style="left:103px">Non-invasive cerebral flow device. Validated in 1,000+ children. Currently in clinical evaluation.</div>
  <div class="abs t-cap" style="left:175px">VELIX explained</div>
  <div class="abs t-capbody mini" style="left:175px">Our probe delivers coherent red light through the skin. The speckle pattern changes with red blood cell motion, resolved by our algorithm.</div>
</section>

<section>
  <div class="abs t-welcome-band"></div>
  <div class="abs t-wphoto" role="img" aria-label="Infant reaching up with small hands" style="background:linear-gradient(150deg,#a5743f,#5a3520 60%,#e2bfa4)"></div>
  <div class="abs t-wlabel">WELCOME</div>
  <div class="abs t-wtext">Now the focus shifts to decreasing disabilities and improving long-term outcomes.</div>
  <div class="abs t-select"><span>PUBLICATIONS</span><span>▾</span></div>
  <div class="abs t-partners">
    <span style="width:26px"></span><span style="width:20px"></span><span style="width:30px"></span><span style="width:28px"></span><span style="width:32px"></span><span style="width:30px"></span>
  </div>
</section>

<section class="abs t-care" role="img" aria-label="Black and white photo of a sleeping newborn cradled by a hand" style="background:linear-gradient(150deg,#555,#222 45%,#888 80%,#444)"></section>
<div class="abs t-care-h" style="top:516px">Current Standard of Care</div>
<div class="abs t-care-list" style="top:527px">TRANSCRANIAL DOPPLER ULTRASOUND<br>• Measures cerebral flow<br>• Not continuous<br>• Detects damage after it occurs<br>• Bulky, interferes with monitoring<br>• Detects larger vessels</div>
<div class="abs t-care-h" style="top:573px">Future Standard of Care</div>
<div class="abs t-care-list" style="top:584px">VELIX<br>• Continuous measurement<br>• Detects issues early<br>• Can measure cortical blood flow<br>• For use in small vessels</div>

<section>
  <div class="abs t-arc"></div>
  <div class="abs t-team" role="img" aria-label="Portrait of a team member in a white coat" style="left:85px;top:667px;background:linear-gradient(180deg,#dfe6ee,#b9c4cf)"></div>
  <div class="abs t-team" role="img" aria-label="Portrait of a team member in a white coat" style="left:158px;top:667px;background:linear-gradient(180deg,#e7e7e7,#a9a29c)"></div>
  <div class="abs t-name" style="left:85px;top:739px">Adrian Holt</div><div class="abs t-role" style="left:85px;top:743px">Co-Founder</div>
  <div class="abs t-name" style="left:158px;top:739px">Nora Whitfield</div><div class="abs t-role" style="left:158px;top:743px">Co-Founder</div>
  <div class="abs t-team" role="img" aria-label="Portrait of a team member with stethoscope" style="left:85px;top:754px;background:linear-gradient(180deg,#e5e9ee,#b5bcc4)"></div>
  <div class="abs t-team" role="img" aria-label="Portrait of a team member with stethoscope" style="left:158px;top:754px;background:linear-gradient(180deg,#8d8b96,#d8d6dc)"></div>
  <div class="abs t-name" style="left:85px;top:826px">Marcus Ellery</div><div class="abs t-role" style="left:85px;top:830px">CEO</div>
  <div class="abs t-name" style="left:158px;top:826px">Lena Park</div><div class="abs t-role" style="left:158px;top:830px">Quality Regulatory</div>
</section>

<section>
  <div class="abs t-contact" role="img" aria-label="Newborn in an incubator under blue hospital light" style="background:linear-gradient(135deg,#5a6ad0,#c9a1b6 40%,#6a7be0 70%,#4b4fb8)"></div>
  <form class="abs t-form">
    <h4>Have questions?<br>Get in touch!</h4>
    <div class="t-field">Name</div><div class="t-field">Email</div><div class="t-field">Subject</div>
    <div class="t-field" style="height:22px">Message</div>
    <div class="t-field" style="border:0;font-size:2px">☐ I agree that my data is being collected and stored</div>
    <div class="t-send">Send Message</div>
  </form>
</section>

<section>
  <div class="abs t-faq-orb"></div>
  <div class="abs t-faq-label">NEED HELP?</div>
  <h3 class="abs t-faq-title">Frequently asked<br>questions</h3>
  <div class="abs t-faq-copy mini">Find quick answers about our sensor, studies and how to work with our team.</div>
  <div class="abs t-faq-list">
    <div><span>How can I get started?</span><span>+</span></div>
    <div><span>Do you offer virtual consultations?</span><span>−</span></div>
    <div style="font-size:2.2px;color:var(--muted)"><span>Yes, our team can meet online at a time that suits you.</span></div>
    <div><span>What industries do you specialize in?</span><span>+</span></div>
    <div><span>Do you work with startups?</span><span>+</span></div>
  </div>
</section>

<footer class="abs t-footer">
  <div class="abs brand"><i></i>Cerevia</div>
  <div class="abs t-fcol" style="left:65px">Office<br>USA —<br>410 Harbor Lane, Suite 12<br>Boston, 02110<br><br>hello@cerevia-labs.com<br><br>+1 555 014 22 80</div>
  <div class="abs t-fcol" style="left:119px">Links<br>Home<br>About<br>Technology<br>Publications<br>Contact</div>
  <div class="abs t-fcol" style="left:173px">Get in Touch<div class="t-fsoc"><i></i><i></i><i></i><i></i></div></div>
  <div class="abs t-fbase"><span>© 2025 Cerevia. All Rights Reserved.</span><span>Privacy Terms</span></div>
</footer>

<!-- ===== Hero ===== -->
<header class="abs hero hero-bg">
  <div class="abs brand"><i></i>Cerevia</div>
  <nav class="abs nav"><span class="active">HOME</span><span>ABOUT</span><span>TECHNOLOGY</span><span>PUBLICATIONS</span><span>CONTACT</span></nav>
  <div class="abs btn-outline-light">Get in Touch</div>
  <div class="abs eyebrow">WELCOME TO CEREVIA - STARTUP</div>
  <h1 class="abs headline">Improving the<br>future for the<br><span>smallest<br>patients</span></h1>
  <div class="abs btn-primary">More Details</div>
  <div class="abs hero-visual" role="img" aria-label="Senior doctor kneeling to hold hands with a toddler in front of a colourful backdrop"></div>
  <div class="abs stat-card"><div class="num">20+</div><hr><p>Years of experience</p></div>
  <div class="abs divider"></div>
  <div class="abs marquee"><span>S</span><b></b><span>TECHNOLOGY FOR PREMATURE INFANTS</span><b></b><span>TECHNOLOGY FOR PREMATURE INFANTS</span><b></b><span>TECHNOLOGY FOR PREMATURE INFANTS</span></div>
</header>

<!-- ===== How we help ===== -->
<section>
  <h2 class="abs help-title">HOW WE HELP</h2>
  <div class="abs help-copy">
    <p>During the first days of life, a significant risk of permanent injury exists from ventricular hemorrhage (IVH), caused by rupture of immature blood vessels in the brain due to excessive flow. There is a clear link between excessive fluctuations in blood flow and subsequent development of IVH.</p>
    <p>VELIX 1 is a continuous intracranial blood flow sensor designed to provide real-time monitoring of blood flow, providing clinicians with an early warning signal to potentially mitigate permanent injury.</p>
  </div>
  <div class="abs btn-outline-dark">Contact Us</div>
  <div class="abs vrule" style="left:638px"></div>
  <div class="abs vrule" style="left:922px"></div>

  <div class="abs card-photo" role="img" aria-label="Crying newborn on a blue blanket being examined by clinician hands" style="left:664px;background:linear-gradient(165deg,#d4b79b 0%,#e9d2bd 30%,#3f67a8 65%,#2b4f8e)"></div>
  <h3 class="abs card-title" style="left:664px">What is it VELIX</h3>
  <div class="abs card-body" style="left:664px">• Non- invasive real- time cerebral blood flow device<br>• Technology validated in 1,000+ children<br>• Exclusive IP license from Northbay Hospital<br>• Currently in clinical evaluation</div>

  <div class="abs card-photo" role="img" aria-label="Premature infant with a nasal feeding tube resting on a parent's chest" style="left:949px;background:linear-gradient(160deg,#cfc6b8 0%,#e0b9a3 35%,#b8705a 70%,#e6d9d2)"></div>
  <h3 class="abs card-title" style="left:949px">VELIX explained</h3>
  <div class="abs card-body" style="left:949px">
    <p>Our probe delivers a small amount of coherent, red light through the skin.</p>
    <p>The resulting reflection pattern has a variable intensity, called speckle, that changes from the motion of red blood cells in the field of exposure. We use a computational algorithm to resolve the relative amount of motion that directly correlates to the blood flow.</p>
  </div>
</section>

<div class="abs bottom-band"></div>
</body>
</html>
```